Boracay Wedding Invitation Design

Hello, We would like a wedding invitation design for our wedding in Boracay. We would like it somewhat in the form of a boarding pass with beachy fresh colours, possibly a nice Boracay beach in the background Double sided with an envelope design to match. Maybe something simple on the envelope like a nice picture in the bottom left corner of a shell on a beach or something similar.

I would also like on the opposite side of the invite to be an "information sheet" with a matching beach design

The text files for both sides are included and i have also included 2 designs that i thought looked nice and are similar to what we are after.
Updates

Hello, I have updated the brief to be more specific with text files and images to make it easier for you. Thank you :)

Industry/Entity Type

Wedding

Font styles to use
Decorative
Script

Colors
fbee3d
33a6d7
33b8a4
fbf289
85cae6
ffffff

Requirements
Must have
• I would like to have this quote somewhere on the invitation
• This day I will marry my best friend,
• the one I laugh with,
• live for,
• dream with,
• love
• Owen & Marisa
• Request the pleasure of your company to celebrate their wedding
• On Friday the 17th March 2017
• at
• Velunda Grand Suites
• Boracay, Philippines
• Ceremony begins at 3.00pm
• RSVP
• Owen 0431907254
• Marisa 0417283649
• by
• 17th Jan 2016
• Dress: Beach Formal
• For the "information sheet"
• There will be a 5% discount on rooms booked at the Velunda under the event Owen & Marisa Wedding. The resort has a total of 24 rooms it would be nice if the majority of guests could stay at the resort from the night before until the night after the wedding but if you choose to stay elsewhere on the island there are plenty of other places to stay for cheaper and everything is fairly close as its a small island.
• We have currently blocked room stay for a short period of time so our guests can book rooms. If you choose to do so please email reservations@velundastays.example. Once rooms become available to the public again, towards the end of Jan, it will be first come first served basis. The resort is very popular so im assuming once this happens the rooms will be booked out.
• If you would like to check out the resort itself the website is www.velundagrand-isle.example
• We know its a fair distance to travel but we would really love to see you all there to celebrate and maybe even enjoy a small holiday while your here its a beautiful part of the world.
• If anyone has any questions please feel free to contact Owen on 0431907254
Nice to have
• A nice picture of a Boracay beach in the background would be nice

```html
<!DOCTYPE html>
<html lang="en">
<head>
<meta charset="utf-8">
<title>Owen &amp; Marisa — Boracay Wedding Invitation</title>
<link rel="stylesheet" href="https://fonts.googleapis.com/css2?family=Great+Vibes&family=Della+Respira&family=Noto+Serif:ital@1&family=Open+Sans&display=swap">
<style>
  :root {
    --stub-yellow: #f8e46a;
    --paper: #f2ede1;
    --paper-edge: #e7dfcc;
    --teal: #33b8a4;
    --ink: #5b5550;
    --stub-ink: #7c775f;
    --cream: #f3eede;
    --map-line: #d8c9b0;
    --palm: #6b6764;
  }
  * { margin: 0; padding: 0; box-sizing: border-box; }
  html, body { width: 1200px; height: 509px; overflow: hidden; background: #fff; }

  .invitation {
    position: relative;
    width: 1200px;
    height: 509px;
    overflow: hidden;
    background: var(--paper);
    font-family: "Della Respira", serif;
  }

  .stub {
    position: absolute;
    left: 0; top: 0;
    width: 112px; height: 509px;
    background: var(--stub-yellow);
  }
  .stub-note {
    position: absolute;
    left: 60px; top: 256px;
    transform: translate(-50%, -50%) rotate(-90deg);
    white-space: nowrap;
    font-family: "Open Sans", sans-serif;
    font-size: 18.5px;
    letter-spacing: 0.2px;
    color: var(--stub-ink);
  }

  .ticket-body {
    position: absolute;
    left: 112px; top: 0;
    width: 782px; height: 509px;
    background: linear-gradient(135deg, #f4f0e6 0%, #efe9dc 55%, #f2ede2 100%);
  }

  .route {
    position: absolute; left: 0; top: 0;
    width: 1200px; height: 509px;
  }

  .ship {
    position: absolute;
    width: 36px; height: 30px;
    border-radius: 4px;
    background: rgba(200, 185, 160, 0.35);
  }
  .ship--top { left: 702px; top: 32px; }
  .ship--bottom { left: 278px; top: 428px; }

  .notch {
    position: absolute;
    width: 30px; height: 30px;
    border-radius: 50%;
    top: 240px;
  }
  .notch--stub { left: 97px; background: var(--stub-yellow); clip-path: inset(0 0 0 50%); }
  .notch--panel { left: 879px; background: var(--teal); clip-path: inset(0 50% 0 0); }

  .greeting {
    position: absolute;
    left: 153px; top: 70px;
    font-size: 18.5px;
    color: var(--ink);
  }

  .couple {
    position: absolute;
    left: 196px; top: 102px;
    font-family: "Great Vibes", cursive;
    font-size: 92px;
    line-height: 1;
    color: var(--teal);
    white-space: nowrap;
  }
  .couple .amp { margin: 0 22px; }

  .details {
    position: absolute;
    left: 153px; top: 254px;
    border-collapse: collapse;
    font-size: 21.5px;
  }
  .details th {
    width: 174px;
    text-align: left;
    font-weight: normal;
    color: var(--teal);
    vertical-align: top;
  }
  .details td { color: var(--ink); }
  .details th, .details td { height: 30.3px; line-height: 30px; white-space: nowrap; }

  .panel {
    position: absolute;
    left: 894px; top: 0;
    width: 306px; height: 509px;
    background: var(--teal);
  }
  .swirl {
    position: absolute;
    left: 47px; top: 0;
    width: 243px; height: 160px;
    border-radius: 0 0 60% 50%;
    background: radial-gradient(ellipse at 55% 40%, rgba(243,238,222,0.55), rgba(243,238,222,0.15) 70%, transparent 75%);
  }
  .vow {
    position: absolute;
    left: 0; top: 219px;
    width: 306px;
    text-align: center;
    font-family: "Noto Serif", serif;
    font-style: italic;
    font-size: 19px;
    line-height: 24.3px;
    color: var(--cream);
  }

  .palms {
    position: absolute;
    left: 772px; top: 312px;
    width: 168px; height: 197px;
    border-radius: 40% 45% 0 0;
    background: linear-gradient(180deg, rgba(107,103,100,0.9) 0%, rgba(107,103,100,0.8) 70%, rgba(150,145,140,0.6) 100%);
  }
</style>
</head>
<body>
<main class="invitation">
  <aside class="stub">
    <p class="stub-note">FULL INFORMATION AVAILABLE AT THE BACK</p>
  </aside>
  <div class="notch notch--stub"></div>

  <section class="ticket-body"></section>

  <svg class="route" viewBox="0 0 1200 509" aria-hidden="true">
    <path d="M870 14 C780 30, 640 90, 600 140 C540 210, 570 250, 600 300 C640 370, 640 430, 560 480 C530 498, 510 505, 500 509"
          fill="none" stroke="var(--map-line)" stroke-width="2.5" stroke-dasharray="12 10"/>
  </svg>
  <div class="ship ship--top" role="img" aria-label="Small sailing ship sketch"></div>
  <div class="ship ship--bottom" role="img" aria-label="Small sailing ship sketch"></div>

  <p class="greeting">we request the pleasure of your company to celebrate our wedding</p>

  <h1 class="couple">Owen<span class="amp">&amp;</span>Marisa</h1>

  <table class="details">
    <tr><th>Date &amp; Time:</th><td>Friday the 17th March 2017, begines at 3.00pm</td></tr>
    <tr><th>Reception Venue:</th><td>Velunda Grand Suites</td></tr>
    <tr><th>Destination</th><td>Boracay, Philippines</td></tr>
    <tr><th>RSVP:</th><td>17th Jan 2016</td></tr>
    <tr><th></th><td>Owen 0431907254</td></tr>
    <tr><th></th><td>Marisa 0417283649</td></tr>
    <tr><th>Dress:</th><td>Beach Formal</td></tr>
  </table>

  <aside class="panel">
    <div class="swirl" role="img" aria-label="Cream flourish ornament of curling swirls"></div>
    <p class="vow">This day<br>I will marry my best friend,<br>the one I laugh with,<br>live for,<br>dream with,<br>love</p>
  </aside>
  <div class="notch notch--panel"></div>

  <div class="palms" role="img" aria-label="Silhouettes of palm trees with birds over the beach"></div>
</main>
</body>
</html>
```